Rate Card

We wish to update our rate card flyer.I have uploaded a copy of our current version, which has a black background but we want to redesign this with a cleaner and fresh look with a white background. Our new logo also needs to be used.

The stats on the why choose us need to be updated also.

- 8,000+ sales agreed
- £2.1bn sales value
- £41m savings
- 97.5% recommended
- 5,000 client testimonials

We would like a new look to this double sided flyer.

This is an urgent requirement so anyone that posts a design we like quickly will more than likely get this order!

```html
<!DOCTYPE html>
<html lang="en">
<head>
<meta charset="utf-8">
<title>Hearthline Homes – Rate Card</title>
<link rel="stylesheet" href="https://fonts.googleapis.com/css2?family=Montserrat:wght@600;700;800&family=Open+Sans:wght@400;600&display=swap">
<style>
  :root {
    --ink: #333333;
    --ink-soft: #555555;
    --backdrop: #000000;
    --card: #ffffff;
    --header-grey: #e3e4e6;
    --pink: #e8398f;
    --blue: #27bfea;
    --green: #8dc63f;
    --purple: #7a3d8f;
    --media-blue: #1aa3d9;
    --media-red: #a3181f;
    --listing-green: #2e9a4a;
    --listing-purple: #5b2a6e;
    --listing-blue: #1b6fb5;
  }
  * { box-sizing: border-box; margin: 0; padding: 0; }
  html, body { width: 852px; height: 1200px; overflow: hidden; }
  body {
    position: relative;
    background: var(--backdrop);
    font-family: "Montserrat", Arial, sans-serif;
    color: var(--ink);
  }
  .side { position: absolute; left: 18px; width: 814px; background: var(--card); }
  .side--front { top: 18px; height: 576px; }
  .side--back { top: 607px; height: 571px; }
  .abs { position: absolute; }

  /* Front: fee menu */
  .fee-title {
    left: 0; width: 100%; top: 60px; text-align: center;
    font-size: 52px; font-weight: 800; letter-spacing: -0.5px; line-height: 1;
  }
  .fee-table {
    left: 69px; top: 157px; width: 675px;
    border-collapse: collapse; table-layout: fixed;
  }
  .fee-table th, .fee-table td {
    border: 2px solid var(--card);
    text-align: center; vertical-align: middle;
    font-weight: 700; color: var(--card);
  }
  .fee-table thead th { background: var(--header-grey); color: var(--ink); font-size: 20px; height: 65px; }
  .fee-table tbody th, .fee-table tbody td { height: 65px; font-size: 21px; }
  .fee-table tbody th { font-size: 20px; }
  .fee-table .cell-note { font-size: 15px; line-height: 1.2; }
  .row-no-commission > * { background: var(--pink); }
  .row-commission > * { background: var(--blue); }
  .row-no-sale > * { background: var(--green); }
  .fee-footnote { right: 68px; top: 426px; font-size: 8px; font-family: "Open Sans", Arial, sans-serif; color: var(--ink); }
  .listings-label { left: 68px; top: 450px; font-size: 15px; font-weight: 700; }
  .listing-badge { top: 492px; height: 26px; border-radius: 4px; }
  .listing-badge--one { left: 66px; width: 135px; background: var(--listing-green); }
  .listing-badge--two { left: 228px; width: 118px; background: var(--listing-purple); }
  .listing-badge--three { left: 372px; width: 124px; background: var(--listing-blue); }
  .brand { left: 558px; top: 476px; display: flex; align-items: center; gap: 8px; }
  .brand-mark { width: 40px; height: 40px; background: var(--pink); flex: none; }
  .brand-name { font-size: 19px; font-weight: 700; color: var(--ink); line-height: 1; }
  .brand-tagline { display: block; font-size: 10.5px; font-weight: 600; color: var(--ink-soft); margin-top: 5px; }

  /* Back: why choose us */
  .why-title { left: 52px; top: 56px; font-size: 50px; font-weight: 800; letter-spacing: -0.5px; line-height: 1; }
  .featured-label { left: 614px; top: 13px; font-size: 16px; font-weight: 700; }
  .media-badge { border-radius: 2px; }
  .media-badge--radio { left: 612px; top: 41px; width: 65px; height: 29px; background: var(--media-blue); }
  .media-badge--news { left: 681px; top: 41px; width: 65px; height: 29px; background: var(--media-red); }
  .media-badge--tv { left: 612px; top: 74px; width: 134px; height: 33px; background: var(--media-red); }
  .col-heading { font-size: 19px; font-weight: 700; line-height: 1.32; }
  .stats-heading { left: 53px; top: 133px; }
  .service-heading { left: 409px; top: 152px; }
  .point-list { list-style: none; font-size: 13.6px; font-weight: 700; color: var(--ink); }
  .point-list li { position: relative; padding-left: 12px; line-height: 19px; margin-bottom: 8.2px; }
  .point-list li::before {
    content: ""; position: absolute; left: 1px; top: 5px;
    border-left: 6px solid var(--ink-soft);
    border-top: 4.5px solid transparent; border-bottom: 4.5px solid transparent;
  }
  .stats-list { left: 53px; top: 193px; width: 330px; }
  .service-list { left: 409px; top: 187px; width: 380px; }
  .review-badge {
    left: 102px; top: 440px; width: 196px; height: 56px;
    background: var(--purple); border-radius: 4px;
  }
  .contact { left: 532px; top: 386px; display: flex; gap: 20px; }
  .contact-mark { width: 48px; height: 48px; background: var(--pink); flex: none; margin-top: 3px; }
  .contact-details { font-family: "Open Sans", Arial, sans-serif; font-size: 12px; line-height: 16.2px; color: var(--ink); font-style: normal; }
  .contact-name { font-size: 14px; font-weight: 600; line-height: 18px; }
  .contact-phone { display: flex; align-items: center; gap: 4px; }
</style>
</head>
<body>

<section class="side side--front" aria-label="Fee menu">
  <h1 class="abs fee-title">fee menu</h1>

  <table class="abs fee-table">
    <colgroup><col style="width:190px"><col style="width:162px"><col style="width:162px"><col style="width:161px"></colgroup>
    <thead>
      <tr><th></th><th>upfront</th><th>completion</th><th>total</th></tr>
    </thead>
    <tbody>
      <tr class="row-no-commission"><th>no commision</th><td>£495+VAT</td><td>£0</td><td>£495+VAT</td></tr>
      <tr class="row-commission"><th>commision</th><td>£195+VAT</td><td>£795+VAT</td><td>£990+VAT</td></tr>
      <tr class="row-no-sale"><th>no sale-no fee</th><td>£0</td><td class="cell-note">we'll beat any<br>quote*</td><td class="cell-note">we'll beat any<br>quote*</td></tr>
    </tbody>
  </table>

  <p class="abs fee-footnote">* subject to a minimum fee of £1000+VAT</p>

  <p class="abs listings-label">Your property advertised on:</p>
  <div class="abs listing-badge listing-badge--one" role="img" aria-label="Property listing portal badge"></div>
  <div class="abs listing-badge listing-badge--two" role="img" aria-label="Property listing portal badge"></div>
  <div class="abs listing-badge listing-badge--three" role="img" aria-label="Property listing portal badge"></div>

  <div class="abs brand">
    <span class="brand-mark" aria-hidden="true"></span>
    <p class="brand-name">Hearthline Homes<span class="brand-tagline">home of the clever seller</span></p>
  </div>
</section>

<section class="side side--back" aria-label="Why choose us">
  <h2 class="abs why-title">why choose us ?</h2>

  <p class="abs featured-label">As Featured on</p>
  <div class="abs media-badge media-badge--radio" role="img" aria-label="Radio station badge"></div>
  <div class="abs media-badge media-badge--news" role="img" aria-label="News channel badge"></div>
  <div class="abs media-badge media-badge--tv" role="img" aria-label="TV news channel badge"></div>

  <h3 class="abs col-heading stats-heading">Strenght in numbers<br>since our launch in 2003</h3>
  <ul class="abs point-list stats-list">
    <li>8,000+ sales agreed</li>
    <li>£2.1bn sales value</li>
    <li>£41m savings vs high street fees</li>
    <li>£4,500 average fee SAVING vs high street</li>
    <li>97.5% recommended by our clients</li>
    <li>5,000 client testimonials</li>
    <li>9/10 average client rating</li>
    <li>Rated no.2 estate agent in the UK by the independent Verdict Hub</li>
  </ul>
  <div class="abs review-badge" role="img" aria-label="Review site rating badge"></div>

  <h3 class="abs col-heading service-heading">Customer service</h3>
  <ul class="abs point-list service-list">
    <li>Personal account manager with direct dial</li>
    <li>Online account to track your progress</li>
    <li>All staff are NPEA qualified</li>
    <li>Weekly activity reports keep you in the loop</li>
    <li>Live web chat facility after hours</li>
    <li>Full personal estate agency service from<br>instruction to completion</li>
  </ul>

  <div class="abs contact">
    <span class="contact-mark" aria-hidden="true"></span>
    <address class="contact-details">
      <div class="contact-name">Hearthline Homes</div>
      Estate Offices<br>
      Ashcombe Mill<br>
      Ashcombe Lane<br>
      Little Brayford<br>
      Essex&nbsp; CM9 4QT<br>
      <span class="contact-phone">
        <svg width="10" height="10" viewBox="0 0 10 10" aria-hidden="true"><path d="M2 0.5 C0.5 1.5 0.5 4 3 6.8 S8.5 9.5 9.5 8 L8 6.3 L6.6 7.2 C5.2 6.5 3.5 4.8 2.8 3.4 L3.7 2 Z" fill="var(--ink)"/></svg>
        01632 960 418
      </span>
      www.hearthlinehomes.co.uk
    </address>
  </div>
</section>

</body>
</html>
```